quorvadeal.com redesign with wireframes, white space and custom form are very important

Need a new two column design that will convert easily to mobile responsive. Lots of white space. Winning design will probably be based on header area and making the custom form stand out. I want the header to be very much like www.talbekmo.com except the form not to go up into the header.
Here are some of the websites I really like:
www.pivrostacks.com
http://glendarokfastmove.com/
http://morquilandestate.com/

We buy homes for cash and close fast. Our target is a home seller who is desperate to sell quickly.
I have uploaded my really ugly wireframe and my logo. I also uploaded my photo for the about us box and a possible photo to use for the header.
The copy on the wireframe is what I will be using except for the about us box.

Here is the exact link for video to frame in the top left box.
https://example-vidhost.net/Kp39xqTzR2a

Number of Pages Required

1 page

Font styles to use
Sans Serif

Colors
0592cd
85cae6
eaf1f7
fbee3d
ec1f27

Requirements
Must have
• Everything on wireframe.
• Must use Verdana font and nothing should be smaller than 12 point. Most should be in 14 point. (except maybe inside of form)

```html
<!DOCTYPE html>
<html lang="en">
<head>
<meta charset="utf-8">
<title>quorvadeal.com – Sell your home for cash</title>
<link rel="stylesheet" href="https://fonts.googleapis.com/css2?family=Open+Sans:wght@400;600;700&family=Libre+Baskerville:ital@0;1&display=swap">
<style>
:root{
  --blue:#0592cd;
  --blue-dark:#0a6fa3;
  --blue-light:#85cae6;
  --ice:#eaf1f7;
  --yellow:#fbee3d;
  --red:#ec1f27;
  --ink:#333b44;
  --grey:#8a9097;
  --field:#c9ccd0;
  --panel:#f2f3f5;
  --line:#dde3ea;
  --white:#ffffff;
}
*{box-sizing:border-box;margin:0;padding:0}
html,body{width:1200px;height:2995px;overflow:hidden;background:var(--white)}
body{font-family:Verdana,"Open Sans",sans-serif;color:var(--ink);font-size:14px;line-height:1.45}
.page{height:2995px;display:flex;flex-direction:column}
.wrap{width:930px;margin:0 auto}
.two-col{display:grid;grid-template-columns:440px 440px;gap:50px}

/* header */
.topbar{height:10px;background:var(--ice)}
.site-header{height:110px;border-bottom:1px solid var(--line);background:linear-gradient(var(--white),var(--ice))}
.site-header .wrap{height:100%;display:flex;align-items:center;gap:46px}
.brand{display:flex;align-items:center;gap:10px;font-family:"Open Sans",sans-serif;font-weight:700;font-size:24px;color:var(--blue-dark)}
.brand-mark{width:22px;height:22px;background:var(--blue)}
.main-nav{display:flex;gap:30px;list-style:none}
.main-nav a{color:var(--blue);text-decoration:none;font-size:13px;letter-spacing:.3px}

/* hero */
.hero{height:380px;position:relative;background:linear-gradient(180deg,#7d95ad 0%,#a9b7c4 38%,#8a7c6c 70%,#5f6a4f 100%);text-align:center;color:var(--white)}
.hero-title{padding-top:110px;font-family:"Libre Baskerville",serif;font-style:italic;font-size:50px;text-shadow:0 2px 6px rgba(0,0,0,.45)}
.hero-sub{margin-top:14px;font-size:24px;font-weight:bold;text-shadow:0 2px 4px rgba(0,0,0,.45)}

/* strip */
.strip{height:58px;background:var(--panel);border-bottom:1px solid var(--line)}
.strip .wrap{height:100%;display:flex;align-items:center;justify-content:space-between}
.strip-note{display:flex;align-items:center;gap:10px;font-size:12px;color:var(--grey)}
.dots{display:flex;gap:5px}
.dots i{width:9px;height:9px;border-radius:50%;background:#9aa1a8;display:block}
.form-tab{width:440px;height:58px;align-self:flex-end;background:var(--blue);color:var(--white);font-weight:bold;font-size:20px;display:flex;align-items:center;justify-content:center;letter-spacing:.5px;box-shadow:0 -3px 0 var(--blue-dark) inset}

/* section 1 */
.intro{padding-top:26px;height:640px}
.h-blue{color:var(--blue);font-weight:bold;font-size:15px}
.benefits{list-style:none;margin:18px 0 34px}
.benefits li{display:flex;align-items:center;gap:12px;margin-bottom:16px;font-size:14px}
.icon-dot{width:26px;height:26px;flex:none}
.video{width:380px;height:250px;margin-left:20px;position:relative;background:linear-gradient(135deg,#2b3440,#556171 55%,#2f3945);border:4px solid var(--ice)}
.video-caption{position:absolute;left:0;right:0;bottom:26px;background:rgba(255,255,255,.85);color:var(--ink);font-size:12px;padding:4px 14px;text-align:right}
.video-play{position:absolute;left:50%;top:42%;transform:translate(-50%,-50%)}

.lead-form{background:var(--panel);padding:12px 26px 26px;border:1px solid var(--line)}
.form-note{text-align:center;font-size:12px;color:var(--grey);margin-bottom:14px}
.field{display:block;width:100%;height:34px;margin-bottom:9px;background:var(--field);border:none;border-radius:2px;padding:0 12px;font-size:12px;font-weight:bold;color:var(--ink);font-family:inherit;line-height:34px}
.field-area{height:64px}
.submit{display:block;margin:16px auto 0;background:var(--blue);color:var(--white);font-size:13px;font-weight:bold;border:none;padding:10px 26px;border-radius:3px;font-family:inherit}

/* section 2 */
.reasons{height:840px;padding-top:30px;border-top:1px solid var(--line)}
.reasons p{margin-bottom:16px}
.reason-list{list-style:none;margin:14px 0 20px}
.reason-list li{display:flex;align-items:center;gap:12px;margin-bottom:18px}
.reason-icon{width:30px;height:30px;flex:none}
.center-blue{text-align:center;color:var(--blue);font-weight:bold}

.privacy-row{display:flex;align-items:center;gap:10px;border-bottom:2px solid var(--blue);padding-bottom:8px}
.privacy-tab{background:var(--blue);color:var(--white);font-weight:bold;font-size:13px;padding:10px 16px}
.social-box{width:34px;height:20px;background:var(--field);border-radius:2px}
.call-us{color:var(--blue);font-weight:bold;font-size:19px;line-height:1.35;margin:22px 0 30px}
.card{border:1px solid var(--line);background:var(--ice);margin-bottom:34px}
.card-head{background:var(--blue);color:var(--white);font-weight:bold;font-size:14px;padding:12px 16px}
.card-body{padding:18px 16px;font-size:13px}
.signature{text-align:right;font-weight:bold;margin-top:12px}
.more-link{display:block;text-align:right;color:var(--blue);text-decoration:underline;margin-top:24px;font-size:13px}
.about{display:flex;gap:16px;align-items:center}
.about-photo{width:74px;height:74px;border-radius:50%;background:linear-gradient(135deg,#b7c3cf,#7f8d9b);flex:none}

/* section 3 */
.blogs{height:590px;padding-top:32px;border-top:1px solid var(--line)}
.blog{background:var(--panel);border:1px solid var(--line);padding:18px 20px;margin-bottom:28px;font-size:13px}
.blog h3{color:var(--blue);font-size:14px;margin-bottom:6px}
.cities{background:var(--panel);border:1px solid var(--line);padding:20px 22px;font-size:13px}
.cities p{margin-bottom:16px}

/* section 4 */
.gallery-row{height:330px;padding-top:10px}
.side-nav{list-style:none}
.side-nav li{background:var(--blue);color:var(--white);font-weight:bold;font-size:13px;padding:11px 16px;margin-bottom:8px;width:240px;box-shadow:3px 3px 0 var(--blue-light)}
.gallery{border:1px solid var(--line);padding:14px 10px}
.gallery h3{text-align:center;color:var(--blue);font-size:14px;margin-bottom:16px}
.gallery-track{display:flex;align-items:center;gap:8px}
.arrow{width:22px;height:60px;background:var(--ice);display:flex;align-items:center;justify-content:center;flex:none}
.thumb{flex:1;height:180px}
.t1{background:linear-gradient(#c9dcec,#a9a08f 60%,#6d7b52)}
.t2{background:linear-gradient(#d5e3ef,#8b7e72 55%,#56623f)}
.t3{background:linear-gradient(#b9d0e6,#7d8a80 55%,#4a5a3a)}
.t4{background:linear-gradient(#cddceb,#b7ab98 60%,#77835a)}

.spacer{flex:1}
.site-footer{height:58px;background:var(--blue);color:var(--white);font-size:13px}
.site-footer .wrap{height:100%;display:flex;align-items:center;justify-content:space-between}
</style>
</head>
<body>
<div class="page">
  <div class="topbar"></div>
  <header class="site-header">
    <div class="wrap">
      <div class="brand"><span class="brand-mark"></span>quorvadeal.com</div>
      <ul class="main-nav">
        <li><a href="#">SELL YOUR HOME</a></li>
        <li><a href="#">HOW IT WORKS</a></li>
        <li><a href="#">STOP FORECLOSURE</a></li>
        <li><a href="#">PROBATE</a></li>
        <li><a href="#">CONTACT</a></li>
      </ul>
    </div>
  </header>

  <section class="hero" role="img" aria-label="Photo of a stucco family home with a tiled roof under an evening sky">
    <h1 class="hero-title">Sell your home for cash in 8 days</h1>
    <p class="hero-sub">We buy Houses Nationwide.</p>
  </section>

  <div class="strip">
    <div class="wrap">
      <div class="strip-note"><span class="dots"><i></i><i></i><i></i></span>We Can Help: We are the fastest home buyers around</div>
      <div class="form-tab">SELL MY HOME FAST!</div>
    </div>
  </div>

  <section class="intro wrap two-col">
    <div>
      <h2 class="h-blue">These are the benefits of selling your home to us.</h2>
      <ul class="benefits">
        <li><svg class="icon-dot" viewBox="0 0 26 26"><circle cx="13" cy="13" r="12" fill="none" stroke="#0592cd" stroke-width="2"/><circle cx="13" cy="13" r="6" fill="none" stroke="#0592cd" stroke-width="2"/><path d="M13 9v4h3" stroke="#0592cd" stroke-width="2" fill="none"/></svg>You pick the closing date</li>
        <li><svg class="icon-dot" viewBox="0 0 26 26"><circle cx="13" cy="13" r="12" fill="none" stroke="#0592cd" stroke-width="2"/><path d="M7 13l4 4 8-8" stroke="#0592cd" stroke-width="2.5" fill="none"/></svg>You pay NO commissions or fees</li>
        <li><svg class="icon-dot" viewBox="0 0 26 26"><circle cx="13" cy="13" r="12" fill="none" stroke="#0592cd" stroke-width="2"/><path d="M7 13l4 4 8-8" stroke="#0592cd" stroke-width="2.5" fill="none"/></svg>You don't have to paint, clean or make repairs</li>
      </ul>
      <div class="video" role="img" aria-label="Embedded video of the owner explaining how the cash home purchase works">
        <svg class="video-play" width="60" height="60" viewBox="0 0 60 60"><circle cx="30" cy="30" r="28" fill="rgba(255,255,255,.25)"/><path d="M24 18l18 12-18 12z" fill="#fff"/></svg>
        <div class="video-caption"><strong>Dale Brenner</strong><br>quorvadeal.com</div>
      </div>
    </div>
    <form class="lead-form">
      <p class="form-note">Get a no-obligation written offer within 24 hours</p>
      <div class="field">Your Name</div>
      <div class="field">Your Phone Number</div>
      <div class="field">Your Address</div>
      <div class="field">Property Address (City, State and Zip Code)</div>
      <div class="field">Repairs needed if any</div>
      <div class="field">Asking price</div>
      <div class="field field-area">Comments</div>
      <button class="submit" type="button">Submit, Sell your home fast »</button>
    </form>
  </section>

  <section class="reasons wrap two-col">
    <div>
      <p class="h-blue">Sell your home or house fast for cash to a professional investor company. We buy Houses and close quickly.</p>
      <p>Selling a home on your own has never been easier. From Orlando to Greensboro - and all points in between - you can sell your home today without any hassles.</p>
      <p>Call 1-800-555-0147 or fill out the form below to get a written offer on your home in just 24 hours.</p>
      <p>Sell today online to people that care.</p>
      <p class="h-blue">If you need to sell a home fast because of:</p>
      <ul class="reason-list">
        <li><svg class="reason-icon" viewBox="0 0 30 30"><circle cx="15" cy="15" r="14" fill="#0592cd"/><path d="M9 15l4 4 8-8" stroke="#fff" stroke-width="2.5" fill="none"/></svg>Divorce or Bankruptcy</li>
        <li><svg class="reason-icon" viewBox="0 0 30 30"><circle cx="15" cy="15" r="14" fill="#0592cd"/><path d="M8 16l7-7 7 7M10 15v7h10v-7" stroke="#fff" stroke-width="2" fill="none"/></svg>Foreclosure</li>
        <li><svg class="reason-icon" viewBox="0 0 30 30"><circle cx="15" cy="15" r="14" fill="#0592cd"/><path d="M8 16l7-7 7 7M10 15v7h10v-7" stroke="#fff" stroke-width="2" fill="none"/></svg>Landlord problems - evictions with tenants okay</li>
        <li><svg class="reason-icon" viewBox="0 0 30 30"><circle cx="15" cy="15" r="14" fill="#0592cd"/><path d="M10 9h10v12H10z M12 13h6M12 16h6" stroke="#fff" stroke-width="2" fill="none"/></svg>Inherited property in probate</li>
        <li><svg class="reason-icon" viewBox="0 0 30 30"><circle cx="15" cy="15" r="14" fill="#0592cd"/><path d="M15 8c4 5 5 7 5 9a5 5 0 0 1-10 0c0-2 1-4 5-9z" fill="#fff"/></svg>Termites, mold, flood or fire damage, leaky roof</li>
        <li><svg class="reason-icon" viewBox="0 0 30 30"><circle cx="15" cy="15" r="14" fill="#0592cd"/><path d="M8 13h14v8H8z M11 13v-3h8v3" stroke="#fff" stroke-width="2" fill="none"/></svg>Moving or can't afford mortgage payments</li>
      </ul>
      <p class="center-blue">We Can Help.<br>We are the fastest home buyers around.</p>
    </div>
    <aside>
      <div class="privacy-row"><span class="privacy-tab">Our Privacy Policy</span><span class="social-box"></span><span class="social-box"></span><span class="social-box"></span></div>
      <p class="call-us">Call us 8am to 10 pm Eastern time.<br>We answer our phones.</p>
      <div class="card">
        <div class="card-head">Home Seller Testimonials</div>
        <div class="card-body">
          <p>I just wanted to thank you for buying my home in Winter Park. You made it fast and easy and kept me well informed the whole way.</p>
          <p class="signature">Harlan Voss – Winter Park</p>
          <a class="more-link" href="#">More Testimonials</a>
        </div>
      </div>
      <div class="card">
        <div class="card-head">About Us</div>
        <div class="card-body about">
          <div class="about-photo" role="img" aria-label="Portrait photo of the company owner"></div>
          <p>Owned and operated in Orlando Florida since 2001. Oldest Continuous operated website in country.</p>
        </div>
      </div>
    </aside>
  </section>

  <section class="blogs wrap two-col">
    <div>
      <article class="blog"><h3>Blog entry 1</h3><p>Lorem ipsum dolor sit amet, reque iriure fabulas et est. At nec suas enim eleifend. Cu vix paulo scaevola, per cibo erat illum ea. Omnis mutat philosophia ut qui.</p></article>
      <article class="blog"><h3>Blog entry 2</h3><p>Lorem ipsum dolor sit amet, reque iriure fabulas et est. At nec suas enim eleifend. Cu vix paulo scaevola, per cibo erat illum ea. Omnis mutat philosophia ut qui.</p></article>
      <article class="blog"><h3>Blog entry 3</h3><p>Lorem ipsum dolor sit amet, reque iriure fabulas et est. At nec suas enim eleifend. Cu vix paulo scaevola, per cibo erat illum ea. Omnis mutat philosophia ut qui.</p></article>
    </div>
    <div class="cities">
      <p class="h-blue">Some of the cities where we buy houses.<br>Not all are listed.</p>
      <p>These are the cities where we have an affiliate where you can sell a home fast or quickly and we buy homes: Orlando Jacksonville Ft Myers Tampa St Pete Gainesville Tallahassee Melbourne West Palm Beach Apopka Deland Kissimmee Lakeland Ocala Chicago Philadelphia Camden Atlanta Valdosta Houston Detroit Phoenix Seattle Tacoma Portland Nashville Cincinnati San Antonio Harrisburg Virginia Beach Virginia Homes Greensboro Charleston SC Flint Rochester Lake Florida Wilmington Columbia Titusville If you don't see your city, we still probably buy homes there.</p>
      <p>These are the types of real estate that we buy: We buy nice houses and outdated problem homes. We buy in great neighborhoods and not so nice. We buy block homes and frame homes.</p>
    </div>
  </section>

  <section class="gallery-row wrap two-col">
    <ul class="side-nav">
      <li>Archives</li>
      <li>Sell my home</li>
      <li>Fast cash for homes</li>
      <li>We buy houses</li>
      <li>Real Estate investor</li>
      <li>Latest</li>
    </ul>
    <div class="gallery">
      <h3>We buy nice pretty houses and some ugly ones as well.</h3>
      <div class="gallery-track">
        <span class="arrow"><svg width="10" height="16" viewBox="0 0 10 16"><path d="M8 2L2 8l6 6" stroke="#0592cd" stroke-width="2.5" fill="none"/></svg></span>
        <div class="thumb t1" role="img" aria-label="Photo of a two-storey white family house"></div>
        <div class="thumb t2" role="img" aria-label="Photo of an older brick house"></div>
        <div class="thumb t3" role="img" aria-label="Photo of a large house behind trees"></div>
        <div class="thumb t4" role="img" aria-label="Photo of a single-storey ranch home"></div>
        <span class="arrow"><svg width="10" height="16" viewBox="0 0 10 16"><path d="M2 2l6 6-6 6" stroke="#0592cd" stroke-width="2.5" fill="none"/></svg></span>
      </div>
    </div>
  </section>

  <div class="spacer"></div>
  <footer class="site-footer">
    <div class="wrap">
      <span>Copyright 2015 · quorvadeal.com · All Rights Reserved</span>
      <strong>1-800-555-0147</strong>
    </div>
  </footer>
</div>
</body>
</html>
```